small auto electrical company needs new logo and business cards !!!

we are a small auto electrical company (Velmor Autos Ltd) that has been running for 13 years the logo we have was put together by dinosaurs so we are looking at re branding the company starting with business cards and a new logo we fit GPS tracking devices for young drivers through there insurance company also we fit hands free systems and dash cameras also safety locks to fleet vehicles we would like bright eye catching colours day glow and neon and quirky designs for the logo our original logo was baby blue which i have added a picture enclosed we would like double sided but have a space to write notes and prices preferably not white on back same colour throughout many thanks
Reason: Just a chance to finalise any designs we want VA logos or V logos - No vlm's and no dinosaurs lol
Business
Installs@velmorautos.co.uk
07922483617
www.Velmorautos.co.uk
Velmor Autos Ltd - Fleets and Insurance Services
- new logo design !!
- Satellite in logo or something attaining to gps
- maybe a car in the logo
- shouldnt have velmor as vlm it is VeLMOR Autos

```html
<!DOCTYPE html>
<html lang="en">
<head>
<meta charset="utf-8">
<title>Velmor Autos Ltd – Business Cards</title>
<link href="https://fonts.googleapis.com/css2?family=Open+Sans:wght@400;600;700&display=swap" rel="stylesheet">
<style>
  :root {
    --backdrop: #3b3431;
    --brand-green: #1e9447;
    --ink: #141414;
    --paper: #ffffff;
  }
  * { box-sizing: border-box; margin: 0; padding: 0; }
  html, body { width: 1200px; height: 780px; overflow: hidden; }
  body {
    background: var(--backdrop);
    font-family: "Open Sans", Arial, sans-serif;
    position: relative;
  }
  .card {
    position: absolute;
    top: 235px;
    width: 530px;
    height: 303px;
    box-shadow: 0 10px 30px rgba(0,0,0,.45);
  }
  .card--front { left: 45px; background: var(--brand-green); }
  .card--back { left: 625px; background: var(--paper); }

  .brand { display: flex; flex-direction: column; align-items: flex-start; }
  .brand__row { display: flex; align-items: center; gap: 10px; }
  .brand__dot { width: 26px; height: 26px; border-radius: 50%; }
  .brand__name { font-weight: 700; font-size: 34px; letter-spacing: -0.5px; line-height: 1; }
  .brand__tagline { font-size: 13px; letter-spacing: 2.2px; margin-top: 6px; margin-left: 2px; }

  .card--front .brand { position: absolute; left: 105px; top: 118px; }
  .card--front .brand__dot { background: var(--ink); }
  .card--front .brand__name { color: var(--paper); }
  .card--front .brand__tagline { color: var(--ink); }

  .card--back .brand { position: absolute; right: 30px; top: 150px; }
  .card--back .brand__name { color: var(--brand-green); font-size: 30px; }
  .card--back .brand__dot { background: var(--brand-green); width: 22px; height: 22px; }
  .card--back .brand__tagline { color: var(--ink); font-size: 11.5px; }

  .person { position: absolute; left: 30px; top: 28px; }
  .person__name { color: var(--brand-green); font-weight: 700; font-size: 17px; }
  .person__role { color: var(--ink); font-size: 14px; margin-top: -2px; }

  .contacts { position: absolute; left: 30px; top: 178px; list-style: none; }
  .contacts li { display: flex; align-items: center; gap: 8px; font-size: 14.5px; color: var(--ink); line-height: 21px; }
  .contacts svg { width: 15px; height: 15px; flex: none; }

  .address { position: absolute; right: 30px; bottom: 26px; font-size: 15px; color: var(--ink); line-height: 20px; }
</style>
</head>
<body>
  <section class="card card--front" aria-label="Card front">
    <div class="brand">
      <div class="brand__row">
        <span class="brand__name">Velmor Autos Ltd</span>
        <span class="brand__dot"></span>
      </div>
      <span class="brand__tagline">Fleet &amp; Insurance Service</span>
    </div>
  </section>

  <section class="card card--back" aria-label="Card back">
    <div class="person">
      <p class="person__name">DANA HOLLIS</p>
      <p class="person__role">Managing Director</p>
    </div>

    <ul class="contacts">
      <li>
        <svg viewBox="0 0 16 16" aria-hidden="true"><rect width="16" height="16" fill="#1e9447"/><path d="M4 4h3l1 3-1.5 1a6 6 0 0 0 2.5 2.5l1-1.5 3 1v3A9 9 0 0 1 4 4z" fill="#fff"/></svg>
        (01) 4820 7316
      </li>
      <li>
        <svg viewBox="0 0 16 16" aria-hidden="true"><rect width="16" height="16" fill="#1e9447"/><rect x="4" y="3" width="8" height="4" fill="#fff"/><rect x="3" y="8" width="10" height="5" fill="#fff"/></svg>
        (01) 4820 7316
      </li>
      <li>
        <svg viewBox="0 0 16 16" aria-hidden="true"><rect width="16" height="16" fill="#1e9447"/><rect x="3" y="4.5" width="10" height="7" fill="#fff"/><path d="M3 4.5l5 4 5-4" stroke="#1e9447" stroke-width="1.2" fill="none"/></svg>
        info@velmorautos.co.uk
      </li>
    </ul>

    <div class="brand">
      <div class="brand__row">
        <span class="brand__name">Velmor Autos Ltd</span>
        <span class="brand__dot"></span>
      </div>
      <span class="brand__tagline">Fleet &amp; Insurance Service</span>
    </div>

    <address class="address" style="font-style:normal">
      PO BOX 418 Harlow Lane<br>
      2nd street Kestrel, USA
    </address>
  </section>
</body>
</html>
```